Yoga By Mirelle Ad for print

I need a print ad designed to go in a brochure for a charity event. I've attached the specs. I need the specs for the 1/2 page ad.
Text for ad:

“E-RYT 200 extensive training with Kestrel Path
Social Media Influencer
Offering group, private and corporate yoga classes
Email: info@yogabymirelle.example
Web: www.yogabymirelle.example
Phone: 555-201-3864
Instagram: @sunlitmatcurls

Target Market(s)

Yoga practitioners and businesses looking to bring yoga in to their operation.

Font styles to use
Serif
Script

Colors
eda3c7
e34197
eea4c8
f9d9e8
feeeee
000000
1b1b1b
cbcbcb
eaeaea

Requirements
Must have
• One version of my logo, I have provided many to choose from for best aesthetic appeal

```html
<!DOCTYPE html>
<html lang="en">
<head>
<meta charset="utf-8">
<title>Yoga By Mirelle – Half Page Ad</title>
<link rel="stylesheet" href="https://fonts.googleapis.com/css2?family=Josefin+Sans:wght@300;400&family=PT+Sans+Narrow:wght@400;700&display=swap">
<style>
  :root {
    --coral: #e8566c;
    --ink: #1b1b1b;
    --text-dark: #1b1b1b;
    --text-light: #ffffff;
    --paper: #ffffff;
    --page: #ffffff;
    --photo-top: #d9b79a;
    --photo-mid: #f49a86;
    --photo-low: #4e8db5;
  }
  * { margin: 0; padding: 0; box-sizing: border-box; }
  html, body {
    width: 1000px; height: 1200px; overflow: hidden;
    background: var(--page);
  }
  .sheet { position: relative; width: 1000px; height: 1200px; }

  .ad {
    position: absolute;
    width: 792px; height: 483px;
    background: var(--paper);
    box-shadow: 0 12px 32px rgba(0,0,0,.16);
    overflow: hidden;
  }
  .ad--first { left: 103px; top: 87px; }
  .ad--second { left: 103px; top: 622px; width: 789px; }

  .ad__dark-panel {
    position: absolute; left: 0; top: 0;
    width: 354px; height: 100%;
    background: var(--ink);
  }

  .brand-mark {
    position: absolute; left: 12px; width: 260px; top: 122px;
    text-align: center;
    font-family: "Josefin Sans", sans-serif;
    font-weight: 400;
    font-size: 38px;
    color: var(--coral);
    letter-spacing: 1px;
    white-space: nowrap;
  }

  .bullet-dot {
    position: absolute;
    width: 7px; height: 7px; border-radius: 50%;
    background: var(--coral);
  }

  .contact {
    position: absolute; left: 12px; width: 260px; top: 270px;
    text-align: center;
    font-family: "PT Sans Narrow", sans-serif;
    font-size: 14.5px; line-height: 17.5px;
    color: var(--text-light);
    white-space: nowrap;
  }

  .photo {
    position: absolute; left: 292px; top: 40px;
    width: 150px; height: 385px;
    border-radius: 40px 40px 20px 20px;
    background: linear-gradient(180deg, var(--photo-top) 0%, var(--photo-mid) 55%, var(--photo-low) 78%, var(--photo-low) 100%);
  }

  .title {
    position: absolute; right: 40px; top: 48px;
    text-align: right;
    font-family: "Josefin Sans", sans-serif;
    font-weight: 300;
    color: var(--coral);
    line-height: 1;
  }
  .title__main { display: block; font-size: 100px; letter-spacing: 1px; }
  .title__line { display: block; margin-top: -6px; white-space: nowrap; }
  .title__small { font-size: 32px; margin-right: 6px; vertical-align: 20px; }
  .title__name { font-size: 58px; letter-spacing: 0.5px; }

  .highlights {
    position: absolute; left: 470px; width: 295px; top: 254px;
    list-style: none; text-align: center;
    font-family: "PT Sans Narrow", sans-serif;
    font-weight: 700;
    font-size: 17.5px; line-height: 21px;
    color: var(--text-dark);
  }
  .highlights li { position: relative; padding-top: 14px; margin-bottom: 7px; }
  .highlights li::before {
    content: ""; position: absolute; top: 2px; left: 50%;
    width: 7px; height: 7px; margin-left: -3.5px;
    border-radius: 50%; background: var(--coral);
  }
  .ad--second .highlights li { margin-bottom: 12px; }
</style>
</head>
<body>
<div class="sheet">

  <section class="ad ad--first">
    <div class="ad__dark-panel"></div>
    <div class="brand-mark">Sunlit Mat</div>
    <span class="bullet-dot" style="left:139px; top:255px;"></span>
    <p class="contact">
      Email: info@yogabymirelle.example<br>
      Web: www.yogabymirelle.example<br>
      Phone: 555-201-3864<br>
      Instagram: @sunlitmatcurls
    </p>
    <div class="photo" role="img" aria-label="Photo of the yoga instructor seated cross-legged with arms stretched overhead"></div>
    <h1 class="title">
      <span class="title__main">YOGA</span>
      <span class="title__line"><span class="title__small">BY</span><span class="title__name">MIRELLE</span></span>
    </h1>
    <ul class="highlights">
      <li>E-RYT 200 extensive training<br>with Kestrel Path</li>
      <li>Social Media Influencer</li>
      <li>Offering group, private<br>and corporate yoga classes</li>
    </ul>
  </section>

  <section class="ad ad--second">
    <div class="ad__dark-panel"></div>
    <div class="brand-mark">Sunlit Mat</div>
    <span class="bullet-dot" style="left:139px; top:240px;"></span>
    <p class="contact" style="top:255px;">
      Email: info@yogabymirelle.example<br>
      Web: www.yogabymirelle.example<br>
      Phone: 555-201-3864<br>
      Instagram: @sunlitmatcurls
    </p>
    <div class="photo" role="img" aria-label="Photo of the yoga instructor seated cross-legged with arms stretched overhead"></div>
    <h1 class="title">
      <span class="title__main">YOGA</span>
      <span class="title__line"><span class="title__small">BY</span><span class="title__name">MIRELLE</span></span>
    </h1>
    <ul class="highlights">
      <li>E-RYT 200 extensive training<br>with Kestrel Path</li>
      <li>Social Media Influencer</li>
      <li>Offering group, private<br>and corporate yoga classes</li>
    </ul>
  </section>

</div>
</body>
</html>
```